【依頼の目的/概要】
電子書籍(plumet)の表紙デザインをお願いします。

【画像サイズ】
表紙ファイルの理想的な寸法は2,560×1,600ピクセルです。

【タイトル】
あの窓辺にまた灯りがともる静かな暮らしの場を一から育てるための手引き

サブキャッチ
~住む人の歩みを一緒に編み直す語らい中心の新しい手法~

【著者】
株式会社MRTOV
代表取締役 江坂 なつえ

【本の内容】
誰もが迎える老いのステージを「自分の人生まんざらでもなかったなぁ」と思っていただける新手法ナラティブアプローチの方法を介護哲学と共に解説しています。

*本文を参考資料として添付します。

【デザイン要望】
特にイメージにこだわりはありませんので、自由な発想でのデザインご応募を楽しみにしています。
*次点、次次点の方への参加報酬を設定いたしました。
*その他、必要な情報がありましたらお問い合わせください。

暖かいイメージが伝わってきます。
一番人気でした。

この度は力作を多数ご提案いただき、有難うございました。
初めてワクトリアを利用させていただいたのですが、たくさんの洗練されたご提案があったこと、はるかに自分の予想を上回りました。
これからも、利用させていただきたいと思いますので、よろしくお願いいたします。

```html
<!DOCTYPE html>
<html lang="ja">
<head>
<meta charset="utf-8">
<title>あの窓辺にまた灯りがともる静かな暮らしの場を一から育てるための手引き</title>
<link rel="stylesheet" href="https://fonts.googleapis.com/css2?family=Noto+Sans+JP:wght@500;700;900&display=swap">
<style>
  :root {
    --paper: #fffdf8;
    --ink: #1e2a48;
    --accent-red: #d3352f;
    --accent-green: #3c9a56;
    --sky: #dcefdc;
    --floor: #ecdcbc;
    --quote-bg: #fbf3df;
    --quote-line: #e6d6b3;
  }
  html, body { margin: 0; padding: 0; overflow: hidden; }
  body { width: 751px; height: 1200px; background: var(--paper); }
  .cover {
    position: relative; width: 751px; height: 1200px; overflow: hidden;
    background: var(--paper);
    font-family: "Noto Sans JP", sans-serif; color: var(--ink);
  }
  .scene-top {
    position: absolute; left: 0; top: 0; width: 330px; height: 190px;
    background: linear-gradient(180deg, var(--sky), #f2f8ee);
  }
  .scene-floor {
    position: absolute; left: 0; bottom: 0; width: 480px; height: 260px;
    background: linear-gradient(180deg, #f3e7cd, var(--floor));
  }
  .title { margin: 0; }
  .vertical {
    position: absolute; writing-mode: vertical-rl; font-weight: 900;
    line-height: 1; white-space: nowrap;
  }
  .title-col-1 { right: 10px; top: 20px; font-size: 52px; }
  .title-col-2 { right: 118px; top: 40px; font-size: 66px; }
  .title-col-3 { left: 318px; top: 522px; font-size: 48px; }
  .emph { color: var(--accent-red); }
  .title-col-1 .emph { font-size: 72px; }
  .title-col-2 .emph { font-size: 80px; }
  .title-col-3 .emph { font-size: 76px; }

  .subtitle { position: absolute; left: 298px; top: 178px; width: 240px; height: 334px; }
  .subtitle svg { position: absolute; left: 0; width: 240px; height: 30px; }
  .subtitle .bracket-top { top: 0; }
  .subtitle .bracket-bottom { bottom: 0; }
  .subtitle-text {
    position: absolute; left: 50%; top: 38px; transform: translateX(-50%);
    margin: 0; height: 262px;
    writing-mode: vertical-rl; font-weight: 700; font-size: 26px; line-height: 1.55;
    color: var(--accent-green); white-space: nowrap;
  }

  .author {
    position: absolute; left: 40px; top: 282px;
    writing-mode: vertical-rl; line-height: 1.35; white-space: nowrap;
  }
  .author .company, .author .role { font-size: 18px; font-weight: 700; text-orientation: upright; }
  .author .name { font-size: 40px; font-weight: 900; letter-spacing: 0.05em; }

  .quote {
    position: absolute; left: 470px; top: 866px; width: 268px; height: 316px; box-sizing: border-box;
    background: var(--quote-bg); border: 2px solid var(--quote-line);
    padding: 20px 14px; font-size: 19px; font-weight: 700; line-height: 1.75; color: var(--ink);
    white-space: nowrap;
  }
  .quote p { margin: 0; }
</style>
</head>
<body>
<main class="cover">
  <div class="scene-top" role="img" aria-label="淡い色の建物が並ぶ街並みのイラスト"></div>
  <div class="scene-floor" role="img" aria-label="暖かな木の床のイラスト"></div>

  <h1 class="title">
    <span class="vertical title-col-1">あの<span class="emph">窓辺</span>にまた<span class="emph">灯り</span>がともる</span>
    <span class="vertical title-col-2">静かな<span class="emph">暮らしの場</span>を</span>
    <span class="vertical title-col-3">一から育てるための<span class="emph">手引き</span></span>
  </h1>

  <div class="subtitle">
    <svg class="bracket-top" viewBox="0 0 240 30" aria-hidden="true"><path d="M6 28 Q120 -10 234 28" fill="none" stroke="var(--accent-green)" stroke-width="5" stroke-linecap="round"/></svg>
    <p class="subtitle-text">住む人の歩みを一緒に<br>編み直す語らい<br>中心の新しい手法</p>
    <svg class="bracket-bottom" viewBox="0 0 240 30" aria-hidden="true"><path d="M6 2 Q120 40 234 2" fill="none" stroke="var(--accent-green)" stroke-width="5" stroke-linecap="round"/></svg>
  </div>

  <div class="author">
    <span class="company">株式会社MRTOV</span><br>
    <span class="role">代表取締役</span><br>
    <span class="name">江坂 なつえ</span>
  </div>

  <aside class="quote">
    <p>「人生の最終ステージを<br>生きる方々の<br>老人ホームという<br>場所での<br>人生を生き切るという<br>大きい枠組みの中での<br>職員のかかわり方の構築」</p>
  </aside>
</main>
</body>
</html>
```